IT Company needs posters designed for our 5 company values & 1 vision statements

We are an IT company (velmorquay.com) who build and support open source applications and products - cloud solutions, system development and mobile applications
We have recently identified our company values and vision, to which we are very proud of and now it's time to live and breathe these.

These posters will be displayed around the office.
As a team, we are an energetic/fun (notice one of our values) bunch, who really enjoy technology, new ways of doing things and giving our insights and learnings back to the IT community & benefits to our customers.

Design objective:
~ looking for a original way to display our value(s)/vision.
~ an accompanying image/design that 'visually' describes the 'value' rather then just text.
~ One poster per value/vision
~ Consistency across the 5 values and 1 vision.
~ Sizes per poster - approx 45 x 30 cms

Any questions please let me know.

Target Market(s)

Internal staff and customers/visitors who are onsite

Industry/Entity Type

It Company

Requirements
Must have
• ~Must display 'value' and 'description of each' on each poster

~One poster per Value & Vision

~ create a sense of fun with this, it's our opportunity to tell people how we really are and what we believe in.
Should not have
• ~ technical representation - just because we are a IT company does not mean we want our values represented in this way.

```html
<!DOCTYPE html>
<html lang="en">
<head>
<meta charset="utf-8">
<title>Committed — Velmorquay Values</title>
<link rel="stylesheet" href="https://fonts.googleapis.com/css2?family=Questrial&display=swap">
<style>
  :root {
    --paper: #ffffff;
    --bubble: #d9fbeb;
    --letter-outline: #80fcc8;
    --word-teal: #2f7f70;
    --tagline-cyan: #5decf6;
    --brand-teal: #1f6b5c;
    --brand-dot: #6ff0f7;
  }
  html, body {
    margin: 0;
    padding: 0;
    width: 1200px;
    height: 776px;
    overflow: hidden;
    background: var(--paper);
  }
  .value-poster {
    position: relative;
    width: 1200px;
    height: 776px;
    overflow: hidden;
    background: var(--paper);
    font-family: "Questrial", "Century Gothic", sans-serif;
  }
  .bubbles, .initial-letter {
    position: absolute;
    inset: 0;
    width: 1200px;
    height: 776px;
  }
  .bubbles circle { fill: var(--bubble); }
  .initial-letter path {
    fill: none;
    stroke: var(--letter-outline);
    stroke-width: 18;
    stroke-linejoin: miter;
  }
  .value-description {
    position: absolute;
    left: 565px;
    top: 280px;
    margin: 0;
    font-size: 29px;
    line-height: 43px;
    font-style: italic;
    font-weight: 400;
    letter-spacing: 0.5px;
    color: var(--tagline-cyan);
  }
  .value-word {
    position: absolute;
    left: 294px;
    top: 462px;
    margin: 0;
    font-size: 188px;
    line-height: 1;
    font-weight: 400;
    letter-spacing: 1px;
    color: var(--word-teal);
  }
  .brand {
    position: absolute;
    right: 32px;
    bottom: 36px;
    display: flex;
    align-items: center;
    gap: 10px;
  }
  .brand-dot {
    width: 16px;
    height: 16px;
    border-radius: 50%;
    background: var(--brand-dot);
  }
  .brand-name {
    font-size: 30px;
    font-weight: 400;
    color: var(--brand-teal);
  }
</style>
</head>
<body>
  <main class="value-poster">
    <svg class="bubbles" viewBox="0 0 1224 790" aria-hidden="true">
      <circle cx="170" cy="87" r="37"/>
      <circle cx="742" cy="140" r="142"/>
      <circle cx="1128" cy="228" r="138"/>
      <circle cx="190" cy="425" r="190"/>
      <circle cx="478" cy="265" r="75"/>
      <circle cx="800" cy="578" r="210"/>
      <circle cx="258" cy="668" r="38"/>
      <circle cx="522" cy="768" r="95"/>
    </svg>

    <p class="value-description">Accountability, Reliability<br>and Commitment to our<br>business and our customers</p>

    <h1 class="value-word"><span class="visually-initial" aria-hidden="true"></span>ommitted</h1>

    <svg class="initial-letter" viewBox="0 0 1224 790" role="img" aria-label="Outlined letter C">
      <path d="M533 222 A272 272 0 1 0 533 534 L490 504 A220 220 0 1 1 490 252 Z"/>
    </svg>

    <div class="brand">
      <span class="brand-dot"></span>
      <span class="brand-name">velmorquay</span>
    </div>
  </main>
</body>
</html>
```